Small business offering independent forensic science consultancy requires flyer and magnet design

We had great success in obtaining a logo design using pixel harbor and we are hoping to draw on your expertise again!

Clearwater Evidence Advisors is a small consultancy business that mainly involves reviewing forensic case files for both the prosecution and defence, and providing expert opinion on the findings in the form of a report, as well as attending court as an expert witness.

Our areas of expertise currently is Forensic Biology (analysis of body fluids), DNA analysis and bloodstain pattern analysis, but this may grow in the future. You can find further information as well as obtain a bit of a feel for the style we are looking for from our website www.clearwaterevidenceadvisors.com.au.

The flyer should be clean and professional looking and we have attached files including our logo and and a Plumtree Text Doc containing the wording for inclusion in the flyer. We have attached an 'ímage feel' document to give you a feel for the types of images we like - but we own all the images on our website, so please contact me if you want to use any of these images and I can send you the files - however are open to any other images in keeping with our website and brand feel.

We will consider various format options such as tri-fold, bi-fold, however,DL sized bi-fold is probably a slight preference. We are also open to suggestions from designers. We would also like to have the capability to modify our wording on the flyer as we have not completely locked it in as yet.

Please note that the brief is also to include the design of a simple advertising magnet to supplement our flyers. They will also be given out separately. The magnet should be a simple design for standard size (90mm x 45mm) magnet, similar to a business card with logo, tagline and contact details (information contained in attached file).

We look forward to seeing your design ideas. Thanks!
Updates

We will be extending the deadline for this project to the 10th January, to allow designers plenty of time given the time of year! 

Thanks to all the designers who have submitted designs so far - as it is the Christmas and New Year period, I will be extending the deadline by one week to allow time for all of you who have accepted my invitation to submit a design.

We will provide individual feedback over the next week to those who have submitted designs. 

We've had some great designs so far - and look forward to seeing some more!

Many thanks!

Hi designers - thanks for the designs submitted so far.  We have provided feedback to all designs under consideration - and welcome re-submissions with the alterations we have suggested.

The deadline will stay at the 10th Jan, so please finalise your designs and re-submit before this date.

We are also still open to considering new designs at this stage.

Kind regards

Marta

Target Market(s)

The criminal law and law enforcement communities including solicitors, barristers, and detectives.

Industry/Entity Type

Advertising

Requirements
Must have
• Clearwater Evidence Advisors Logo
Clearwater Evidence Advisors Tagline
At least one of the images from our website
Nice to have
• Other images that fit with the picture scheme on our website and in the reference pictures attached.
Should not have
• pictures of fingerprints, deceased, glamorised crime scenes, police or vbq references.

```html
<!DOCTYPE html>
<html lang="en">
<head>
<meta charset="utf-8">
<title>Clearwater Evidence Advisors – Flyer and Magnet</title>
<link rel="stylesheet" href="https://fonts.googleapis.com/css2?family=Questrial&display=swap">
<style>
  :root {
    --stage: #e3e4e6;
    --blue-deep: #0d5fb8;
    --blue-mid: #2a86d8;
    --blue-pale: #d8eaf8;
    --ice: #f4f9fd;
    --ink: #3b4652;
    --ink-strong: #1f2a36;
    --logo-ink: #1c4f8f;
    --photo-a: #2a2f7a;
    --photo-b: #8a3fb0;
    --pill-a: #0b3f86;
    --pill-b: #3a6fc8;
  }
  * { box-sizing: border-box; margin: 0; padding: 0; }
  html, body { width: 1200px; height: 1028px; overflow: hidden; }
  body {
    background: var(--stage);
    font-family: "Questrial", "Century Gothic", sans-serif;
    color: var(--ink);
    position: relative;
  }

  /* ---------- Flyer front ---------- */
  .flyer-front {
    position: absolute; left: 83px; top: 98px;
    width: 489px; height: 466px; overflow: hidden;
    background: linear-gradient(160deg, var(--blue-pale) 0%, var(--ice) 55%, var(--blue-pale) 100%);
    box-shadow: 0 3px 10px rgba(0,0,0,.25);
  }
  .flyer-front .shape { position: absolute; inset: 0; }
  .shape-band { background: #ffffff; clip-path: polygon(100% 2%, 100% 52%, 0 80%, 0 64%); }
  .shape-top { background: linear-gradient(135deg, var(--blue-deep), var(--blue-mid)); clip-path: polygon(0 0, 68% 0, 0 39%); }
  .shape-bottom { background: linear-gradient(90deg, var(--blue-mid), var(--blue-deep)); clip-path: polygon(0 66%, 47% 85%, 100% 85%, 100% 100%, 0 100%); }
  .shape-photo { background: linear-gradient(135deg, var(--photo-a), var(--photo-b) 60%, #c7584a); clip-path: polygon(100% 52.5%, 100% 85%, 47% 85%); }

  .brand {
    position: absolute; display: flex; align-items: center; gap: 8px;
    color: var(--logo-ink); font-weight: 400; line-height: 1.05;
  }
  .brand-dot { border-radius: 50%; background: var(--blue-deep); flex: none; }
  .flyer-front .brand { left: 232px; top: 148px; font-size: 21px; }
  .flyer-front .brand-dot { width: 36px; height: 36px; }

  .contact-front {
    position: absolute; left: 40px; top: 246px; width: 300px;
    text-align: center; font-size: 9.5px; line-height: 1.55;
    color: var(--ink-strong); font-weight: 700;
  }
  .tagline-front {
    position: absolute; left: 244px; top: 408px; width: 150px;
    color: #fff; font-size: 11.5px; line-height: 1.2;
  }

  /* ---------- Flyer inside ---------- */
  .flyer-inside {
    position: absolute; left: 707px; top: 98px;
    width: 457px; height: 466px; overflow: hidden;
    background: linear-gradient(180deg, var(--blue-pale) 0%, #fff 30%, #fff 70%, var(--blue-pale) 100%);
    box-shadow: 0 3px 10px rgba(0,0,0,.25);
    font-size: 9.3px; line-height: 1.27;
  }
  .column { position: absolute; top: 0; width: 200px; }
  .column-left { left: 18px; }
  .column-right { left: 248px; }
  .pill {
    position: absolute; height: 28px; border-radius: 14px;
    background: linear-gradient(90deg, var(--pill-a), var(--pill-b) 70%, var(--photo-b));
    color: #fff; font-size: 10.5px; letter-spacing: 1px; font-weight: 700;
    display: flex; align-items: center; justify-content: flex-end; padding-right: 16px;
  }
  .pill-about { left: 13px; top: 27px; width: 142px; }
  .pill-services { left: 13px; top: 196px; width: 142px; }
  .pill-who { left: 311px; top: 302px; width: 140px; }
  .copy { position: absolute; }
  .copy p { margin-bottom: 7px; }
  .copy ul { list-style: none; margin-bottom: 7px; }
  .copy li { padding-left: 8px; text-indent: -8px; }
  .copy li::before { content: "• "; }

  /* ---------- Magnet ---------- */
  .magnet {
    position: absolute; left: 870px; top: 740px;
    width: 294px; height: 153px; overflow: hidden;
    background: linear-gradient(180deg, #fff 0%, var(--ice) 50%, var(--blue-pale) 100%);
    box-shadow: 0 2px 8px rgba(0,0,0,.25);
  }
  .magnet .brand { left: 14px; top: 16px; font-size: 15px; gap: 6px; }
  .magnet .brand-dot { width: 28px; height: 28px; }
  .magnet-band {
    position: absolute; left: 0; top: 74px; width: 100%; height: 17px;
    background: var(--blue-deep); color: #fff;
    font-size: 8.3px; text-align: center; line-height: 17px; letter-spacing: .2px;
  }
  .magnet-contact {
    position: absolute; left: 78px; top: 98px; width: 200px;
    text-align: center; font-size: 9.6px; line-height: 1.2; color: var(--ink-strong);
  }
</style>
</head>
<body>

<section class="flyer-front" aria-label="Flyer front cover">
  <div class="shape shape-band"></div>
  <div class="shape shape-bottom"></div>
  <div class="shape shape-photo" role="img" aria-label="Laboratory photograph of test tubes in violet light"></div>
  <div class="shape shape-top"></div>

  <div class="brand"><span class="brand-dot"></span><span>Clearwater<br>Evidence Advisors</span></div>

  <address class="contact-front" style="font-style:normal">
    PO Box 3817 Riverbend<br>
    NSW Australia 2190<br>
    Phone: +61 400 555 017<br>
    enquiries@clearwaterevidenceadvisors.com.au<br>
    www.clearwaterevidenceadvisors.com.au
  </address>

  <p class="tagline-front">Forensic Science Expertise from the Crime Scene to Court</p>
</section>

<section class="flyer-inside" aria-label="Flyer inside spread">
  <div class="pill pill-about">ABOUT US</div>
  <div class="copy" style="left:18px; top:70px; width:200px;">
    <p>Our forensic biology experts each have over 10 years experience in operational forensic laboratories, (including the Harlow Forensic Laboratory in the United Kingdom, National Investigations Bureau, and the Coastal State Police Service) and are experts in human biological material (including Blood, Saliva, Semen), Bloodstain Pattern Analysis as well as DNA analysis and interpretation.</p>
  </div>

  <div class="pill pill-services">SERVICES</div>
  <div class="copy" style="left:18px; top:236px; width:200px;">
    <p style="margin-bottom:0">Clearwater Evidence Advisors has expertise in the following areas:</p>
    <ul>
      <li>Forensic Biology (including biological fluid detection techniques</li>
      <li>Bloodstain Pattern Analysis</li>
      <li>Damage Analysis</li>
      <li>DNA Analysis and Interpretation</li>
    </ul>
    <p style="margin-bottom:0">We have the ability to:</p>
    <ul>
      <li>Conduct an independent review of the work conducted by the State or Federal Laboratories</li>
      <li>Assess if all appropriate examinations have been conducted</li>
      <li>Provide an expert opinion in relation to the significance of the evidence</li>
      <li>Assist in providing appropriate lines of questioning for expert witnesses</li>
    </ul>
  </div>

  <div class="copy" style="left:248px; top:12px; width:200px;">
    <ul>
      <li>Appear in court as an expert witness</li>
      <li>Perform laboratory based examinations or re-examinations items for biological evidence.</li>
      <li>Conduct bespoke training on forensic biology, DNA analysis and interpretation and forensic science</li>
    </ul>
    <p style="margin-top:10px; margin-bottom:0">We will provide high quality and timely advice that is honest and transparent and any resulting reports will be presented in a form readily understood by non-scientific audiences. Clearwater Evidence Advisors has implemented a quality framework and is structured to provide the same internal technical review processes required by accrediting bodies such as LABCERT and we are continually working to expand our services and ensure our work is of the highest quality.</p>
    <p>We believe our experience from the crime scene to the court and our quality framework offers our clients one of the most comprehensive independent forensic services available in the area of forensic biology and DNA analysis.</p>
  </div>

  <div class="pill pill-who">WHO USES US?</div>
  <div class="copy" style="left:248px; top:342px; width:200px;">
    <p style="margin-bottom:0">Our services are utilised across the legal and law enforcement communities, some of the organisations that we have completed work for include:</p>
    <ul>
      <li>Private law firms</li>
      <li>Legal Aid</li>
      <li>Aboriginal Legal Aid</li>
      <li>Universities</li>
    </ul>
  </div>
</section>

<section class="magnet" aria-label="Advertising magnet">
  <div class="brand"><span class="brand-dot"></span><span>Clearwater<br>Evidence Advisors</span></div>
  <div class="magnet-band">FORENSIC SCIENCE EXPERTISE FROM THE CRIME SCENE TO COURT</div>
  <address class="magnet-contact" style="font-style:normal">
    PO Box 3817 Riverbend NSW Australia 2190<br>
    Phone: +61 400 555 017<br>
    enquiries@clearwaterevidenceadvisors.com.au<br>
    www.clearwaterevidenceadvisors.com.au
  </address>
</section>

</body>
</html>
```